Display Ad for Local Publication

We have never advertised before but now I would like to have an ad running in our local, community magazine. Our business is Cedar Hollow Mini Storage located in Harbor Point, WA. PL is a small community (+/-2,500 people located across the Puget Sound from Seattle. The monthly magazine, The Tidings, covers all kinds of local news and activities and carries a number of ads from local businesses. Our is the only mini storage in Harbor Point. We have enclosed storage units of various sizes and outdoor parking spaces for boats, trailers and RVs. I am enclosing a business card and the size requirements for Tidings advertisements. I want to develop a 1/8 page ad.

```html
<!DOCTYPE html>
<html lang="en">
<head>
<meta charset="utf-8">
<title>Cedar Hollow Mini Storage – Display Ad</title>
<link rel="stylesheet" href="https://fonts.googleapis.com/css2?family=Montserrat:ital,wght@1,400;1,700;1,800&display=swap">
<style>
  :root {
    --page-bg: #cbcbcb;
    --ad-white: #ffffff;
    --bar-dark: #38383a;
    --brand-green: #4fba6f;
    --title-green: #3fae5f;
    --title-dark: #444446;
    --text-dark: #48484a;
    --text-light: #ffffff;
    --photo-sky: #c6d0da;
    --photo-snow: #e6ebf2;
  }
  * { box-sizing: border-box; margin: 0; padding: 0; }
  html, body {
    width: 1200px;
    height: 829px;
    overflow: hidden;
    background: var(--page-bg);
    font-family: "Montserrat", Arial, sans-serif;
  }
  .ad {
    position: absolute;
    left: 188px;
    top: 166px;
    width: 833px;
    height: 517px;
    background: var(--ad-white);
    display: flex;
    flex-direction: column;
    overflow: hidden;
  }
  .rule-bar { background: var(--bar-dark); flex: none; }
  .rule-bar--top { height: 16px; }
  .rule-bar--mid { height: 12px; }

  .masthead {
    position: relative;
    height: 200px;
    flex: none;
  }
  .masthead__photo {
    position: absolute;
    right: 0;
    top: 0;
    width: 246px;
    height: 100%;
    background:
      linear-gradient(to right, var(--ad-white) 0%, rgba(255,255,255,0) 35%),
      linear-gradient(to bottom, var(--photo-sky) 0%, #aab5bf 45%, var(--photo-snow) 62%, #f1f4f9 100%);
  }
  .business-name {
    position: absolute;
    left: 50px;
    top: 28px;
    z-index: 1;
    font-style: italic;
    font-weight: 800;
    line-height: 1;
  }
  .business-name__primary {
    display: block;
    font-size: 84px;
    letter-spacing: -1px;
    color: var(--title-green);
  }
  .business-name__secondary {
    display: block;
    font-size: 62px;
    margin-top: -4px;
    color: var(--title-dark);
  }

  .pitch {
    height: 174px;
    flex: none;
    background: var(--brand-green);
    color: var(--text-light);
    padding: 18px 0 0 48px;
    font-style: italic;
    font-size: 30px;
    line-height: 35px;
  }
  .pitch__line { display: block; font-weight: 700; }
  .pitch__tagline { display: block; font-weight: 400; }

  .contact {
    flex: 1;
    display: flex;
    padding: 23px 0 0 48px;
    color: var(--text-dark);
    font-style: italic;
    font-weight: 700;
    font-size: 28.5px;
    line-height: 35px;
  }
  .contact__address {
    display: flex;
    width: 315px;
    font-style: italic;
  }
  .contact__lines { display: block; }
  .contact__list { list-style: none; }
  .contact__item { display: flex; align-items: center; }
  .icon {
    flex: none;
    width: 18px;
    height: 22px;
    margin-right: 10px;
    fill: var(--brand-green);
  }
  .contact__address .icon { margin-top: 6px; margin-right: 8px; }
  .contact__item .icon { width: 22px; margin-right: 15px; }
</style>
</head>
<body>
  <article class="ad">
    <div class="rule-bar rule-bar--top"></div>

    <header class="masthead">
      <h1 class="business-name">
        <span class="business-name__primary">Cedar Hollow</span>
        <span class="business-name__secondary">Mini Storage</span>
      </h1>
      <div class="masthead__photo" role="img" aria-label="Photo of the storage facility: rows of roll-up unit doors in snow with evergreen trees behind"></div>
    </header>

    <section class="pitch">
      <span class="pitch__line">The only mini storage facility in Harbor Point.</span>
      <span class="pitch__line">Clean, secure enclosed units in multiple sizes</span>
      <span class="pitch__line">plus outdoor parking for boats, trailers and RVs.</span>
      <span class="pitch__tagline">Easy access. Locally owned.</span>
    </section>

    <div class="rule-bar rule-bar--mid"></div>

    <footer class="contact">
      <address class="contact__address">
        <svg class="icon" viewBox="0 0 22 26" aria-hidden="true">
          <path d="M11 0C5 0 1 4.3 1 9.6 1 16.5 11 26 11 26s10-9.5 10-16.4C21 4.3 17 0 11 0zm0 14a4.3 4.3 0 1 1 0-8.6A4.3 4.3 0 0 1 11 14z"/>
        </svg>
        <span class="contact__lines">812 Alder Lane,<br>Harbor Point, WA</span>
      </address>
      <ul class="contact__list">
        <li class="contact__item">
          <svg class="icon" viewBox="0 0 26 26" aria-hidden="true">
            <path d="M6 2l4 5.5-2.4 2.6c1.5 3.3 4 5.8 7.3 7.3l2.6-2.4L23 19l-2.3 4.3C20 24.5 18.6 25 17 24.6 9.6 22.6 3.4 16.4 1.4 9 1 7.4 1.5 6 2.7 5.3z"/>
            <path d="M15 1.5a10 10 0 0 1 9.5 9.5h-2.2A7.8 7.8 0 0 0 15 3.7zM15 6a5.5 5.5 0 0 1 5 5h-2.2A3.3 3.3 0 0 0 15 8.2z"/>
          </svg>
          360-555-0173
        </li>
        <li class="contact__item">
          <svg class="icon" viewBox="0 0 26 20" aria-hidden="true">
            <path d="M0 2v16h26V2zm3 2.2l10 7.4 10-7.4v.1L13 14 3 4.3z"/>
          </svg>
          rent@chministorage.com
        </li>
      </ul>
    </footer>
  </article>
</body>
</html>
```